Notary Signing Agent Need Business card Design

Need a Business card design for my new company. RT Velo-Brisk LLC
Mobile Notary Signing Agent. I go to the customer for closing of Mortgage's Documents . possible signs of honesty, integrity and confidentiality.

Work with Title company to Notary Mortgage closing.

My Target Market is Title companies. Banks and Financial Institution.

Color Blue to Black Professional ) if needed some Green Little Red

And possible a company logo.

Mobile ( travel to clients ) Integrity, Honest Trustworthy. A show of Professional services.

Would like company name and my name on card

Use both sides and front with business name and my name. phone numbers.

Target Market(s)

Title company, Banks mortgage company

Industry/Entity Type

Travel

Contact Information for Business Card

Notary, Certified signing agent, Mobile

Colors
0455a3

Requirements
Must have
• Name of company , owners name phone number,
Nice to have
• blue and black color like a professional look but not limit to these only.
• a stand out from other cards .

```html
<!DOCTYPE html>
<html lang="en">
<head>
<meta charset="utf-8">
<title>RT Velo-Brisk LLC – Business Card</title>
<link href="https://fonts.googleapis.com/css2?family=Exo+2:ital,wght@0,400;0,500;1,400;1,500&display=swap" rel="stylesheet">
<style>
  :root {
    --page: #ffffff;
    --crop: #9a9a9a;
    --card-top: #3b566d;
    --card-mid-a: #a7b0b5;
    --card-mid-b: #d2d5d2;
    --card-low: #8e9f93;
    --card-bottom: #45604f;
    --brand: #1d4556;
    --ink: #1b2026;
    --accent-faint: rgba(40, 85, 90, 0.22);
  }
  html, body {
    margin: 0;
    padding: 0;
    overflow: hidden;
    background: var(--page);
  }
  .sheet {
    position: relative;
    width: 954px;
    height: 1200px;
    background: var(--page);
    overflow: hidden;
    font-family: "Exo 2", sans-serif;
  }
  .crop-marks {
    position: absolute;
    inset: 0;
  }
  .crop-marks line {
    stroke: var(--crop);
    stroke-width: 1.2;
  }
  .card {
    position: absolute;
    left: 115px;
    width: 723px;
    height: 422px;
    overflow: hidden;
    background: linear-gradient(180deg,
      var(--card-top) 0%,
      var(--card-mid-a) 44%,
      var(--card-mid-b) 58%,
      var(--card-low) 78%,
      var(--card-bottom) 100%);
    color: var(--ink);
  }
  .card--front { top: 118px; }
  .card--back { top: 655px; }
  .card__accent {
    position: absolute;
    left: 560px;
    top: 270px;
    width: 130px;
    height: 130px;
    background: var(--accent-faint);
  }
  .brand-name {
    position: absolute;
    left: 0;
    right: 0;
    text-align: center;
    margin: 0;
    font-weight: 500;
    font-style: normal;
    color: var(--brand);
    letter-spacing: -0.5px;
    white-space: nowrap;
    line-height: 1;
  }
  .card--front .brand-name {
    top: 176px;
    font-size: 100px;
  }
  .card--back .brand-name {
    top: 90px;
    font-size: 82px;
  }
  .contact {
    position: absolute;
    left: 0;
    right: 0;
    top: 182px;
    text-align: center;
  }
  .contact__name {
    margin: 0;
    font-size: 38px;
    font-weight: 400;
    line-height: 1.05;
  }
  .contact__role {
    margin: 2px 0 0;
    font-size: 21px;
    font-style: italic;
    line-height: 1.1;
  }
  .contact__phones {
    margin: 14px 0 0;
    font-size: 17px;
    letter-spacing: 1.5px;
    line-height: 1.3;
  }
</style>
</head>
<body>
<div class="sheet">
  <svg class="crop-marks" width="954" height="1200" viewBox="0 0 954 1200" aria-hidden="true">
    <line x1="115" y1="0" x2="115" y2="82"/>
    <line x1="838" y1="0" x2="838" y2="82"/>
    <line x1="15" y1="118" x2="82" y2="118"/>
    <line x1="871" y1="118" x2="940" y2="118"/>
    <line x1="15" y1="540" x2="82" y2="540"/>
    <line x1="871" y1="540" x2="940" y2="540"/>
    <line x1="115" y1="570" x2="115" y2="625"/>
    <line x1="838" y1="570" x2="838" y2="625"/>
    <line x1="15" y1="655" x2="82" y2="655"/>
    <line x1="871" y1="655" x2="940" y2="655"/>
    <line x1="15" y1="1077" x2="82" y2="1077"/>
    <line x1="871" y1="1077" x2="940" y2="1077"/>
    <line x1="115" y1="1110" x2="115" y2="1200"/>
    <line x1="838" y1="1110" x2="838" y2="1200"/>
  </svg>

  <section class="card card--front">
    <div class="card__accent" aria-hidden="true"></div>
    <h1 class="brand-name">RT Velo-Brisk</h1>
  </section>

  <section class="card card--back">
    <div class="card__accent" aria-hidden="true"></div>
    <p class="brand-name">RT Velo-Brisk</p>
    <div class="contact">
      <p class="contact__name">Daniel R. Hoyt</p>
      <p class="contact__role">Notary Signing Agent</p>
      <p class="contact__phones">850-555-0142<br>850-555-0187</p>
    </div>
  </section>
</div>
</body>
</html>
```